Industrial Services company needs a business card design

We provide industrial maintenance services including sandblasting, painting, pressure washing, storage tank rehabilitation, and welding. I would like an industrial design that's eye catching. I would like the back-side of the card to list our services.

Industry/Entity Type

Construction

Contact Information for Business Card

address: 418 Bramblewood Lane, York, PA 17408
Phone: 410-637-1584
email: quellaninc@mailbrook.net
Walter Brennigan, President
www.quellanpainting.net

Logo Text

Quellan Industrial Services

Font styles to use
Sans Serif

Colors
000000
229ed3
0692cd
ffffff

Requirements
Must have
• Easy to read
• our services listed/included on back of card
• eye catching color combinations
Nice to have
• Water storage tank image

```html
<!DOCTYPE html>
<html lang="en">
<head>
<meta charset="utf-8">
<title>Quellan Inc. – Business Card</title>
<link href="https://fonts.googleapis.com/css2?family=Jost:ital,wght@0,400;0,500;0,700;1,400&display=swap" rel="stylesheet">
<style>
  :root {
    --page-bg: #e9eaeb;
    --brand-blue: #0a93cd;
    --brand-blue-deep: #0880b6;
    --back-blue: #36a8da;
    --back-strip: #0a7fb5;
    --ink: #111111;
    --tagline: #163a4e;
    --white: #ffffff;
    --link-blue: #1596cf;
  }
  * { margin: 0; padding: 0; box-sizing: border-box; }
  html, body {
    width: 993px; height: 1200px; overflow: hidden;
    background: var(--page-bg);
    font-family: "Jost", sans-serif;
  }
  .canvas { position: relative; width: 993px; height: 1200px; }

  .card { position: absolute; width: 931px; height: 558px; overflow: hidden; }
  .card--front { left: 33px; top: 31px; background: var(--white); }
  .card--back { left: 31px; top: 607px; background: var(--back-blue); }

  /* front */
  .front-panel {
    position: absolute; left: 0; top: 0; width: 468px; height: 100%;
    background: var(--brand-blue);
    border-left: 18px solid var(--brand-blue-deep);
  }
  .front-art {
    position: absolute; left: 468px; top: 0; width: 463px; height: 100%;
    background: linear-gradient(200deg, #0d4fa8 0%, #3f8fd6 25%, #a9d2f0 50%, #eef6fc 72%, #ffffff 100%);
  }
  .wordmark {
    position: absolute; color: var(--white);
    font-weight: 700; letter-spacing: 1px; line-height: 1; white-space: nowrap;
  }
  .front-panel .wordmark { left: 20px; top: 40px; font-size: 55px; }
  .tagline {
    position: absolute; font-style: italic; font-weight: 400;
    color: var(--tagline); font-size: 25px; white-space: nowrap;
  }
  .front-panel .tagline { left: 20px; top: 118px; }
  .contact-person { position: absolute; left: 20px; top: 368px; color: var(--white); }
  .contact-person .name { color: var(--ink); font-size: 37px; font-weight: 500; line-height: 50px; }
  .contact-person .role { font-size: 37px; font-weight: 500; line-height: 50px; }
  .contact-person .line { font-size: 25px; line-height: 36px; }

  .front-address { position: absolute; left: 545px; top: 345px; color: var(--link-blue); }
  .front-address .mini-mark { font-size: 20px; font-weight: 700; line-height: 30px; color: var(--brand-blue-deep); }
  .front-address .line { font-size: 28px; line-height: 39px; }

  /* back */
  .back-art {
    position: absolute; left: 52px; top: 22px; width: 820px; height: 523px;
    background: radial-gradient(ellipse at 30% 55%, rgba(30,110,170,0.28), rgba(54,168,218,0) 70%);
  }
  .back-strip { position: absolute; right: 0; top: 0; width: 20px; height: 100%; background: var(--back-strip); }
  .back-content { position: absolute; left: 0; top: 0; width: 911px; height: 100%; text-align: center; }
  .card--back .wordmark { left: 0; right: 0; top: 20px; font-size: 56px; text-align: center; }
  .card--back .tagline { left: 0; right: 0; top: 101px; text-align: center; }
  .services-intro { position: absolute; left: 0; right: 0; top: 178px; font-size: 34px; color: var(--ink); }
  .services-list { position: absolute; left: 0; right: 0; top: 222px; list-style: none; color: var(--white); font-size: 34px; line-height: 43.5px; }
  .back-footer {
    position: absolute; left: 0; right: 0; top: 503px;
    color: var(--white); font-size: 20px; text-align: center; word-spacing: 1px;
  }
  .back-footer .sep { margin: 0 22px; }
</style>
</head>
<body>
<main class="canvas">

  <section class="card card--front" aria-label="Card front">
    <div class="front-panel">
      <div class="wordmark">QUELLAN INC.</div>
      <div class="tagline">Commercial &amp; Industrial Painting</div>
      <div class="contact-person">
        <div class="name">Walter Brennigan,</div>
        <div class="role">President</div>
        <div class="line">Phone: 410-637-1584</div>
        <div class="line">email: quellaninc@mailbrook.net</div>
      </div>
    </div>
    <div class="front-art" role="img" aria-label="Abstract blue faceted crystal pattern fading to white"></div>
    <div class="front-address">
      <div class="mini-mark">QUELLAN INC.</div>
      <div class="line">Address:</div>
      <div class="line">418 Bramblewood Lane,</div>
      <div class="line">York, PA 17408</div>
      <div class="line">www.quellanpainting.net</div>
    </div>
  </section>

  <section class="card card--back" aria-label="Card back">
    <div class="back-art" role="img" aria-label="Faint illustration of a workman holding a wrench beside a sink"></div>
    <div class="back-strip"></div>
    <div class="back-content">
      <div class="wordmark">QUELLAN INC.</div>
      <div class="tagline">Commercial &amp; Industrial Painting</div>
      <p class="services-intro">We provide industrial maintenance services including</p>
      <ul class="services-list">
        <li>Sandblasting</li>
        <li>Painting</li>
        <li>Pressure washing</li>
        <li>Storage tank rehabilitation, and</li>
        <li>Welding</li>
      </ul>
      <p class="back-footer">Phone: 410-637-1584<span class="sep">|</span>email: quellaninc@mailbrook.net<span class="sep">|</span>www.quellanpainting.net</p>
    </div>
  </section>

</main>
</body>
</html>
```